International gaming entertainment company is looking for an innovative Power Point design *

We are looking for a Power Point design for potential international investors, partners and customers in the gaming industry, meaning that a reference to internationality and gaming should become apparent.
The template should be in a reduced and clear style with a combination of innovation and tradition. It should be adaptive and suitable for various applications (tables, shapes and diagrams).
The color scheme of our company are various shades of gray and burgundy (wine-red), however as for the design in question, we are open to other meaningful suggestions (no garish colors).
Updates

Noch kein Design dabei, dass uns 100%ig überzeugt

Target Market(s)

International investors and partners in the gaming industry

Font styles to use
Serif
Sans Serif
Other font styles liked:
• Interstate

Requirements
Must have
• Clear lines
Modern
Footer line with room for classification (eg Confidential, Public) and page number

```html
<!DOCTYPE html>
<html lang="en">
<head>
<meta charset="utf-8">
<title>Vantor Games – Presentation Template Overview</title>
<link rel="stylesheet" href="https://fonts.googleapis.com/css2?family=Barlow:wght@400;600;700&family=Roboto:wght@400;500;700&display=swap">
<style>
:root{
  --wine:#c4122f;
  --wine-mid:#9a1532;
  --wine-deep:#6e1430;
  --plum:#3b2330;
  --ink:#2f2f33;
  --grey:#6d6d72;
  --soft:#f6e3e6;
  --paper:#ffffff;
}
*{margin:0;padding:0;box-sizing:border-box}
html,body{width:1200px;height:675px;overflow:hidden;background:var(--paper)}
body{position:relative;font-family:"Roboto",Arial,sans-serif;color:var(--ink)}
.slide{position:absolute;overflow:hidden;background:var(--paper);box-shadow:0 2px 10px rgba(160,30,50,.12)}
.slide--large{left:76px;width:520px;height:292px}
.slide--small{width:243px;height:137px}
.col-a{left:620px}.col-b{left:881px}
.row-1{top:34px}.row-2{top:189px}.row-3{top:349px}.row-4{top:505px}
.abs{position:absolute}
.heading{position:absolute;left:12px;top:14px;font-family:"Barlow",sans-serif;font-weight:700;font-size:11px;color:var(--wine)}
.tiny{font-size:3px;line-height:3.6px;color:var(--grey)}
.tiny b{color:var(--wine);font-weight:700}
.page-no{position:absolute;right:12px;bottom:5px;font-size:3px;color:#999}
.red-bg{background:linear-gradient(100deg,var(--wine) 0%,var(--wine-mid) 45%,var(--plum) 100%)}
.arc{position:absolute;border-radius:50%;background:rgba(255,255,255,.06)}
/* title */
.cover-photo{position:absolute;inset:0;background:radial-gradient(ellipse at 85% 45%,#5a2a30 0%,#2b1a22 45%,transparent 70%),linear-gradient(100deg,#c21a33 0%,#a01632 40%,#4a1e2a 75%,#281a20 100%)}
.brand{position:absolute;left:26px;top:24px;font-family:"Barlow",sans-serif;font-weight:700;font-size:11px;color:#fff}
.cover-title{position:absolute;left:26px;top:140px;font-family:"Barlow",sans-serif;font-weight:700;font-size:28px;color:#fff;letter-spacing:-.2px}
.cover-date{position:absolute;left:26px;top:178px;font-size:9px;color:#fff}
/* thank you */
.thanks-title{position:absolute;left:26px;top:30px;font-family:"Barlow",sans-serif;font-weight:700;font-size:23px;color:#fff}
.thanks-copy{position:absolute;left:26px;top:67px;width:310px;font-size:7.3px;line-height:8.2px;color:#fff}
.social{position:absolute;display:flex;align-items:center;gap:6px;font-size:6.5px;color:#fff}
.social i{width:15px;height:15px;border:1.3px solid #fff;border-radius:3px;display:block}
.large-page{position:absolute;left:490px;top:273px;font-size:6px;color:#fff}
/* misc small */
.num{position:absolute;width:14px;height:14px;border-radius:50%;background:var(--wine);color:#fff;font-size:6px;font-weight:700;display:flex;align-items:center;justify-content:center;box-shadow:0 0 0 2px #f3d5da}
.plan{position:absolute;top:54px;width:57px;height:68px;background:linear-gradient(160deg,var(--wine-mid),var(--wine-deep));color:#fff;padding:4px 5px}
.plan h4{font-size:4.4px;font-weight:400;line-height:5px}
.plan p{font-size:2.6px;line-height:3.3px;margin-top:3px}
.plan .cta{position:absolute;left:0;bottom:0;width:44px;height:7px;background:#e7d7da;color:var(--wine);font-size:2.6px;padding:2px 4px}
.icon-dot{position:absolute;width:22px;height:22px;border-radius:50%;background:var(--wine);box-shadow:0 0 0 2px #eee;display:flex;align-items:center;justify-content:center}
.icon-dot.dark{background:#4a4a4f}
.list-item{position:absolute;left:12px;display:flex;align-items:center;gap:4px;font-size:4.8px;font-weight:700;color:var(--wine)}
.list-item span{width:8px;height:8px;background:var(--wine);color:#fff;font-size:4px;display:flex;align-items:center;justify-content:center}
.list-item:nth-child(odd) span{background:var(--wine-deep)}
.wheel-label{position:absolute;width:55px;font-size:2.7px;line-height:3.2px;color:var(--grey)}
.wheel-label b{display:block;font-size:4.6px;line-height:5px;color:var(--wine)}
.overview-no{position:absolute;left:1126px;top:637px;font-family:"Barlow",sans-serif;font-size:13px;color:#aaa;letter-spacing:1px}
</style>
</head>
<body>

<!-- cover -->
<section class="slide slide--large row-1">
  <div class="cover-photo" role="img" aria-label="Photo of a gamer wearing a glowing headset in front of monitors, tinted wine red"></div>
  <div class="arc" style="left:130px;top:-60px;width:360px;height:360px"></div>
  <div class="brand">Vantor Games</div>
  <h1 class="cover-title">Presentation Template</h1>
  <div class="cover-date">June 2020</div>
</section>

<!-- thank you -->
<section class="slide slide--large red-bg" style="top:349px">
  <div class="arc" style="left:245px;top:-30px;width:420px;height:420px"></div>
  <div class="arc" style="left:435px;top:40px;width:180px;height:240px;background:rgba(0,0,0,.12)"></div>
  <h2 class="thanks-title">Thank You</h2>
  <p class="thanks-copy">Lorem ipsum dolor sit amet, consectetur adipiscing elit. Aenean quis magna sit amet diam viverra aliquam. Suspendisse placerat justo vel est blandit, sit amet laoreet dui rhoncus. Etiam ex tortor, faucibus a maximus et, commodo non ex. Vestibulum a cursus massa. Morbi dolor diam, vulputate at porttitor sit amet, laoreet in elit. Integer ante felis, mollis vitae nunc quis, bibendum ullamcorper nisi. Donec pellentesque facilisis ex, id cursus elit. Class aptent taciti sociosqu ad litora torquent per conubia nostra, per inceptos himenaeos. Pellentesque gravida dolor vitae magna hendrerit vulputate. Nam porttitor aliquam purus. Quisque neque purus, blandit condimentum ultricies in, tincidunt a mauris. Nam quis nisl risus.</p>
  <div class="social" style="left:26px;top:148px"><i></i>pictola</div>
  <div class="social" style="left:112px;top:148px"><i></i>workmesh</div>
  <div class="social" style="left:26px;top:177px"><i></i>vidstream</div>
  <div class="social" style="left:112px;top:177px"><i></i>chirpline</div>
  <div class="large-page">10</div>
</section>

<!-- 2 introduce -->
<section class="slide slide--small col-a row-1 red-bg">
  <div class="arc" style="left:115px;top:-20px;width:170px;height:170px"></div>
  <div class="abs" style="left:12px;top:67px;font-family:Barlow,sans-serif;font-weight:700;font-size:10px;color:#fff">Introduce</div>
  <div class="abs" style="left:12px;top:84px;font-size:3.2px;color:#fff">Section 1</div>
  <div class="page-no" style="color:#ddd">2</div>
</section>

<!-- 3 numbered list -->
<section class="slide slide--small col-b row-1">
  <div class="heading">Slide Example</div>
  <p class="abs tiny" style="left:12px;top:35px;width:70px"><b>Lorem ipsum dolor sit amet, consectetur adipiscing elit. Aenean quis magna sit amet diam viverra aliquam. Suspendisse placerat justo vel est blandit, sit amet laoreet dui rhoncus.</b> Etiam ex tortor, faucibus a maximus et, commodo non ex. Vestibulum a cursus massa.<br><br>Morbi dolor diam, vulputate at porttitor sit amet, laoreet in elit. Integer ante felis, mollis vitae nunc quis, bibendum ullamcorper nisi. Donec pellentesque facilisis ex, id cursus elit. Class aptent taciti sociosqu ad litora torquent per conubia nostra.</p>
  <div class="num" style="left:88px;top:35px">1</div>
  <div class="num" style="left:88px;top:56px">2</div>
  <div class="num" style="left:88px;top:77px">3</div>
  <div class="num" style="left:88px;top:98px">4</div>
  <p class="abs tiny" style="left:107px;top:36px;width:36px"><b>Lorem ipsum dolor sit amet, consectetur</b> adipiscing elit. Aenean quis magna sit amet.</p>
  <p class="abs tiny" style="left:107px;top:57px;width:36px"><b>Lorem ipsum dolor sit amet, consectetur</b> adipiscing elit. Aenean quis magna sit amet.</p>
  <p class="abs tiny" style="left:107px;top:78px;width:36px"><b>Lorem ipsum dolor sit amet, consectetur</b> adipiscing elit. Aenean quis magna sit amet.</p>
  <p class="abs tiny" style="left:107px;top:99px;width:36px"><b>Lorem ipsum dolor sit amet, consectetur</b> adipiscing elit. Aenean quis magna sit amet.</p>
  <div class="abs" role="img" aria-label="Photo of a game controller in deep wine red light" style="left:147px;top:27px;width:84px;height:93px;background:linear-gradient(150deg,#7a1a2e,#4a1220)"></div>
  <div class="page-no">3</div>
</section>

<!-- 4 pricing cards -->
<section class="slide slide--small col-a row-2">
  <div class="heading">Slide Example</div>
  <p class="abs" style="left:12px;top:33px;width:220px;font-size:3.6px;line-height:4.3px;color:var(--ink)">Choose your service. DeskFlow provides a complete workstation in the thin client model. <b style="color:var(--wine)">All you need is a monitor to start working.</b> Both services can be used encrypted from any location with an existing PC, laptop or tablet.</p>
  <div class="abs" style="left:0;top:67px;width:243px;height:42px;background:var(--soft)"></div>
  <div class="plan" style="left:29px"><h4>THIN<br>CLIENT</h4><p>Features<br>✓ Billing per user<br>✓ Thin client per user included<br>✓ Licensing of the Nimbus operating system<br>✓ Max. 8 hours reaction time</p><div class="cta">GET STARTED NOW</div></div>
  <div class="plan" style="left:93px"><h4>MOBILE<br>THIN CLIENT</h4><p>Features<br>✓ Billing per user<br>✓ Thin client per user included<br>✓ Licensing of the Nimbus operating system<br>✓ Max. 8 hours reaction time</p><div class="cta">GET STARTED NOW</div></div>
  <div class="plan" style="left:157px"><h4>BRING<br>YOUR OWN</h4><p>Features<br>✓ Billing per user<br>✓ Thin client per user included<br>✓ Licensing of the Nimbus operating system<br>✓ Max. 8 hours reaction time</p><div class="cta">GET STARTED NOW</div></div>
  <div class="page-no">4</div>
</section>

<!-- 5 globe -->
<section class="slide slide--small col-b row-2">
  <div class="heading">Slide Example</div>
  <p class="abs tiny" style="left:12px;top:42px;width:50px;color:var(--ink)"><b style="color:var(--ink)">Lorem ipsum dolor sit amet, consectetur adipiscing elit. Aenean quis magna sit amet diam viverra aliquam. Suspendisse placerat justo vel est blandit, sit amet laoreet dui rhoncus.</b> Etiam ex tortor, faucibus a maximus et, commodo non ex. Vestibulum a cursus massa. Morbi dolor diam, vulputate at porttitor sit amet, laoreet in elit.</p>
  <div class="abs" role="img" aria-label="Illustrated globe with world map in shades of red" style="left:65px;top:40px;width:74px;height:74px;border-radius:50%;background:radial-gradient(circle at 35% 35%,#f2b8c2,#d9556d 55%,#a8203b)"></div>
  <div class="icon-dot" style="left:153px;top:39px"><svg width="9" height="9" viewBox="0 0 10 10"><path d="M5 1 L9 2.5 V5 C9 7.5 5 9 5 9 C5 9 1 7.5 1 5 V2.5Z" fill="#fff"/><path d="M3.2 5 L4.5 6.3 L7 3.8" stroke="var(--wine)" stroke-width="1" fill="none"/></svg></div>
  <div class="icon-dot dark" style="left:153px;top:67px;background:var(--wine-mid)"><svg width="9" height="9" viewBox="0 0 10 10"><rect x="2" y="4.5" width="6" height="4.5" fill="#fff"/><path d="M3.3 4.5 V3 A1.7 1.7 0 0 1 6.7 3 V4.5" stroke="#fff" stroke-width="1" fill="none"/></svg></div>
  <div class="icon-dot dark" style="left:153px;top:95px"><svg width="9" height="9" viewBox="0 0 10 10"><circle cx="5" cy="5" r="3.5" stroke="#fff" stroke-width="1" fill="none"/><circle cx="5" cy="5" r="1.3" fill="#fff"/></svg></div>
  <p class="abs tiny" style="left:181px;top:42px;width:52px"><b style="color:var(--ink)">Lorem ipsum dolor sit amet, consectetur</b> adipiscing elit. Aenean quis magna sit amet diam.</p>
  <p class="abs tiny" style="left:181px;top:70px;width:52px"><b style="color:var(--ink)">Lorem ipsum dolor sit amet, consectetur</b> adipiscing elit. Aenean quis magna sit amet diam.</p>
  <p class="abs tiny" style="left:181px;top:98px;width:52px"><b style="color:var(--ink)">Lorem ipsum dolor sit amet, consectetur</b> adipiscing elit. Aenean quis magna sit amet diam.</p>
  <div class="page-no">5</div>
</section>

<!-- 6 line chart -->
<section class="slide slide--small col-a row-3">
  <div class="heading">Slide Example</div>
  <p class="abs" style="left:12px;top:41px;width:100px;font-size:3.2px;line-height:3.8px;color:var(--ink)"><b>Lorem ipsum dolor sit amet, consectetur</b> adipiscing elit. Aenean quis magna sit amet diam.</p>
  <svg class="abs" style="left:10px;top:50px" width="160" height="75" viewBox="0 0 160 75">
    <rect x="2" y="4" width="28" height="8" fill="#e9e2e4"/>
    <polyline points="8,43 22,40 36,37 50,33 64,30 78,27 92,22 106,18 120,14 134,11 148,8" fill="none" stroke="var(--wine)" stroke-width=".8"/>
    <polyline points="8,58 22,55 36,52 50,50 64,48 78,47 92,44 106,42 120,40 134,38 148,37" fill="none" stroke="var(--wine-deep)" stroke-width=".8"/>
    <polyline points="8,62 22,59 36,56 50,54 64,52 78,50 92,48 106,46 120,43 134,41 148,39" fill="none" stroke="#555" stroke-width=".8"/>
    <g fill="var(--wine)"><circle cx="8" cy="43" r="1"/><circle cx="36" cy="37" r="1"/><circle cx="64" cy="30" r="1"/><circle cx="92" cy="22" r="1"/><circle cx="120" cy="14" r="1"/><circle cx="148" cy="8" r="1"/></g>
    <g fill="#555"><circle cx="8" cy="62" r="1"/><circle cx="36" cy="56" r="1"/><circle cx="64" cy="52" r="1"/><circle cx="92" cy="48" r="1"/><circle cx="120" cy="43" r="1"/><circle cx="148" cy="39" r="1"/></g>
    <g font-size="2.6" fill="#555" font-family="Roboto,sans-serif" text-anchor="middle">
      <text x="8" y="71">Mar 26</text><text x="22" y="71">Mar 27</text><text x="36" y="71">Mar 28</text><text x="50" y="71">Mar 29</text><text x="64" y="71">Mar 30</text><text x="78" y="71">Mar 31</text><text x="92" y="71">Mar 01</text><text x="106" y="71">Mar 02</text><text x="120" y="71">Mar 03</text><text x="134" y="71">Mar 04</text>
    </g>
    <g font-size="2.2" fill="#555" font-family="Roboto,sans-serif"><text x="152" y="8">MALAYSIA</text><text x="152" y="37">INDONESIA</text><text x="152" y="40">THAILAND</text></g>
  </svg>
  <div class="num" style="left:179px;top:40px">1</div>
  <div class="num" style="left:179px;top:69px;background:var(--wine-deep)">2</div>
  <div class="num" style="left:179px;top:97px;background:#4a4a4f">3</div>
  <p class="abs tiny" style="left:197px;top:41px;width:38px"><b style="color:var(--ink)">Lorem ipsum dolor sit amet, consectetur</b> adipiscing elit. Aenean quis magna.</p>
  <p class="abs tiny" style="left:197px;top:70px;width:38px"><b style="color:var(--ink)">Lorem ipsum dolor sit amet, consectetur</b> adipiscing elit. Aenean quis magna.</p>
  <p class="abs tiny" style="left:197px;top:98px;width:38px"><b style="color:var(--ink)">Lorem ipsum dolor sit amet, consectetur</b> adipiscing elit. Aenean quis magna.</p>
  <div class="page-no">6</div>
</section>

<!-- 7 wheel -->
<section class="slide slide--small col-b row-3">
  <div class="heading">Slide Example</div>
  <svg class="abs" style="left:79px;top:33px" width="84" height="84" viewBox="-42 -42 84 84">
    <g transform="rotate(-112.5)">
      <circle r="30.5" fill="none" stroke="var(--wine-deep)" stroke-width="23"/>
      <circle r="30.5" fill="none" stroke="var(--wine)" stroke-width="23" stroke-dasharray="23.95 23.95"/>
    </g>
    <g stroke="#fff" stroke-width="1.2">
      <line y1="-19" y2="-42" transform="rotate(22.5)"/><line y1="-19" y2="-42" transform="rotate(67.5)"/><line y1="-19" y2="-42" transform="rotate(112.5)"/><line y1="-19" y2="-42" transform="rotate(157.5)"/><line y1="-19" y2="-42" transform="rotate(202.5)"/><line y1="-19" y2="-42" transform="rotate(247.5)"/><line y1="-19" y2="-42" transform="rotate(292.5)"/><line y1="-19" y2="-42" transform="rotate(337.5)"/>
    </g>
    <g fill="#fff"><circle cx="0" cy="-30" r="2.4"/><circle cx="21" cy="-21" r="2.4"/><circle cx="30" cy="0" r="2.4"/><circle cx="21" cy="21" r="2.4"/><circle cx="0" cy="30" r="2.4"/><circle cx="-21" cy="21" r="2.4"/><circle cx="-30" cy="0" r="2.4"/><circle cx="-21" cy="-21" r="2.4"/></g>
    <circle r="18" fill="#fff"/>
    <text y="-2" text-anchor="middle" font-family="Barlow,sans-serif" font-weight="700" font-size="5" fill="var(--wine)">Main</text>
    <text y="3.5" text-anchor="middle" font-family="Barlow,sans-serif" font-weight="700" font-size="5" fill="var(--wine)">Core</text>
    <text y="7.5" text-anchor="middle" font-family="Roboto,sans-serif" font-size="2" fill="#666">The quick brown fox</text>
    <text y="10" text-anchor="middle" font-family="Roboto,sans-serif" font-size="2" fill="#666">jumps over the lazy</text>
  </svg>
  <div class="wheel-label" style="left:18px;top:38px;text-align:right"><b>Title Edit</b>The quick brown fox jumps over the lazy dog.</div>
  <div class="wheel-label" style="left:18px;top:59px;text-align:right"><b>Title Edit</b>The quick brown fox jumps over the lazy dog.</div>
  <div class="wheel-label" style="left:18px;top:80px;text-align:right"><b>Title Edit</b>The quick brown fox jumps over the lazy dog.</div>
  <div class="wheel-label" style="left:18px;top:101px;text-align:right"><b>Title Edit</b>The quick brown fox jumps over the lazy dog.</div>
  <div class="wheel-label" style="left:172px;top:38px"><b>Title Edit</b>The quick brown fox jumps over the lazy dog.</div>
  <div class="wheel-label" style="left:172px;top:59px"><b>Title Edit</b>The quick brown fox jumps over the lazy dog.</div>
  <div class="wheel-label" style="left:172px;top:80px"><b>Title Edit</b>The quick brown fox jumps over the lazy dog.</div>
  <div class="wheel-label" style="left:172px;top:101px"><b>Title Edit</b>The quick brown fox jumps over the lazy dog.</div>
  <div class="page-no">7</div>
</section>

<!-- 8 list + location -->
<section class="slide slide--small col-a row-4">
  <div class="heading">Slide Example</div>
  <p class="abs" style="left:12px;top:36px;width:105px;font-size:4.3px;line-height:5px;color:var(--grey)"><b style="color:var(--wine)">Lorem Ipsum is simply dummy text of the printing and typesetting industry.</b> Lorem Ipsum has been the industry's standard dummy text ever since the 1500s.</p>
  <div>
    <div class="list-item" style="top:65px"><span>1</span>Business Essentials</div>
    <div class="list-item" style="top:80px"><span>2</span>Marketing Essentials</div>
    <div class="list-item" style="top:94px"><span>3</span>Business Leaders</div>
    <div class="list-item" style="top:109px"><span>4</span>Corporate Finance &amp; Accounting</div>
  </div>
  <div class="abs red-bg" style="left:133px;top:0;width:110px;height:137px">
    <div class="abs" role="img" aria-label="Map of service regions with location markers" style="left:28px;top:20px;width:52px;height:75px;border-radius:40% 45% 35% 45%;background:linear-gradient(160deg,rgba(255,255,255,.35),rgba(255,255,255,.15))"></div>
    <div class="abs" style="left:10px;top:107px;display:flex;align-items:center;gap:3px;font-size:5.2px;font-weight:500;color:#fff">
      <svg width="4" height="5" viewBox="0 0 8 10"><path d="M4 0 A4 4 0 0 1 8 4 C8 7 4 10 4 10 C4 10 0 7 0 4 A4 4 0 0 1 4 0Z" fill="#fff"/><circle cx="4" cy="4" r="1.5" fill="var(--wine)"/></svg>Services Location</div>
    <p class="abs" style="left:17px;top:115px;width:80px;font-size:2.5px;line-height:3px;color:#fff">A business is defined as an organization or enterprising entity engaged in commercial, industrial, or professional activities.</p>
    <div class="page-no" style="color:#ddd">8</div>
  </div>
</section>

<!-- 9 inspiration -->
<section class="slide slide--small col-b row-4">
  <div class="abs" role="img" aria-label="Photo of a backlit gaming keyboard in dark purple and red tones" style="inset:0;background:radial-gradient(ellipse at 15% 70%,#6a3a52 0%,transparent 55%),linear-gradient(120deg,#3a1a2a 0%,#5a1a30 50%,#3a1a3a 100%)"></div>
  <div class="heading" style="color:#fff">Slide Example</div>
  <div class="abs" style="left:80px;top:30px;width:68px;text-align:right;font-family:Barlow,sans-serif;color:#fff;line-height:.95">
    <div style="font-size:14px;font-weight:400">“ YOU</div>
    <div style="font-size:14px;font-weight:400">CAN’T</div>
    <div style="font-size:20px;font-weight:700">STOP</div>
    <div style="font-size:20px;font-weight:700">US.</div>
  </div>
  <div class="abs" style="left:159px;top:29px;font-family:Barlow,sans-serif;font-weight:700;font-size:9px;color:#fff">INSPIRATION</div>
  <p class="abs" style="left:159px;top:40px;width:72px;font-size:2.8px;line-height:3.3px;color:#fff">Lorem ipsum dolor sit amet, consectetur adipiscing elit. Nullam vestibulum interdum ligula vitae laoreet.</p>
  <div class="abs" style="left:159px;top:62px;width:36px;color:#fff"><div style="font-family:Barlow,sans-serif;font-weight:700;font-size:5.8px">1. KEEP</div><p style="font-size:2.3px;line-height:2.8px">Lorem ipsum dolor sit amet, consectetur adipiscing elit. Nullam vestibulum ligula.</p></div>
  <div class="abs" style="left:198px;top:62px;width:36px;color:#fff"><div style="font-family:Barlow,sans-serif;font-weight:700;font-size:5.8px">2. MOVE</div><p style="font-size:2.3px;line-height:2.8px">Lorem ipsum dolor sit amet, consectetur adipiscing elit. Nullam vestibulum ligula.</p></div>
  <div class="abs" style="left:159px;top:90px;width:36px;color:#fff"><div style="font-family:Barlow,sans-serif;font-weight:700;font-size:5.8px">3. TOP</div><p style="font-size:2.3px;line-height:2.8px">Lorem ipsum dolor sit amet, consectetur adipiscing elit. Nullam vestibulum ligula.</p></div>
  <div class="abs" style="left:198px;top:90px;width:36px;color:#fff"><div style="font-family:Barlow,sans-serif;font-weight:700;font-size:5.8px">4. BEING</div><p style="font-size:2.3px;line-height:2.8px">Lorem ipsum dolor sit amet, consectetur adipiscing elit. Nullam vestibulum ligula.</p></div>
  <div class="page-no" style="color:#ccc">9</div>
</section>

<div class="overview-no">11</div>
</body>
</html>
```